Lark & Dew honey company needs a label design.

We need a label design for a new honey company, based in the state of Florida called 'Lark & Dew". We are supplying our online customers with the highest quality of the various kinds of raw honey. Our product is honey in the oval hexagon glass jar with black lid. We would like to see designs that use black background with gold font .
In the upper part of the label is gold flying Honey Bee (profile, silhouette). The name of the brand "Lark & Dew" - Caramel font. Additional fonts are Cinzel, Source Sans Pro. Label measurements 2.6" by 3".
Label content:
Lark & Dew
RAW HONEY
wildflower
PURE & NATURAL
made by Florida Bees
larkanddewhoney.com
NET WT 12oz (340g)

The final design should have eye catching, luxurious look.

Target Market(s)

Luxury

Industry/Entity Type

Food (bee products)

Font styles to use
Other font styles liked:
• caramel

Colors

Designer to choose colors to be used in the design.

Requirements
Must have
• Gold letters on black background, Drawing of a bee, flying in profile

```html
<!DOCTYPE html>
<html lang="en">
<head>
<meta charset="utf-8">
<title>Lark &amp; Dew Raw Honey Label</title>
<link href="https://fonts.googleapis.com/css2?family=Cinzel:wght@400;500&family=Source+Sans+3:wght@400;500&display=swap" rel="stylesheet">
<style>
  :root {
    --backdrop-light: #e6e6e6;
    --backdrop-dark: #cfcfcf;
    --band-dark: #2a2a2a;
    --band-mid: #646464;
    --copper: #b8783f;
    --copper-light: #d8ab7c;
    --cream: #f4efe8;
    --soft-white: #e4e4e4;
  }
  * { margin: 0; padding: 0; box-sizing: border-box; }
  html, body {
    width: 1200px;
    height: 1200px;
    overflow: hidden;
  }
  body {
    background: radial-gradient(circle at 50% 45%, var(--backdrop-light), var(--backdrop-dark));
    position: relative;
    font-family: "Source Sans 3", "Source Sans Pro", sans-serif;
  }
  .label {
    position: absolute;
    left: 50px;
    top: 195px;
    width: 1100px;
    height: 810px;
    background: linear-gradient(90deg,
      var(--band-dark) 0%,
      #3a3a3a 20%,
      var(--band-mid) 52%,
      #4a4a4a 78%,
      var(--band-dark) 100%);
  }
  .label-frame {
    position: absolute;
    left: 305px;
    top: 71px;
    width: 519px;
    height: 659px;
    border: 5px solid var(--copper);
  }
  .bee-illustration {
    position: absolute;
    left: 586px;
    top: 0;
    width: 190px;
    height: 156px;
    border-radius: 50%;
    background: radial-gradient(ellipse at 55% 55%, #8a5a3a 0%, #c98f55 45%, rgba(201,143,85,0) 72%);
  }
  .brand-name {
    position: absolute;
    left: 305px;
    width: 519px;
    top: 185px;
    text-align: center;
    font-weight: 500;
    font-size: 80px;
    line-height: 1;
    color: var(--copper);
  }
  .quality-note {
    position: absolute;
    left: 305px;
    width: 519px;
    top: 345px;
    text-align: center;
    font-family: "Cinzel", serif;
    font-size: 26px;
    letter-spacing: 3px;
    color: var(--cream);
  }
  .product-name {
    position: absolute;
    left: 305px;
    width: 519px;
    top: 392px;
    text-align: center;
    font-family: "Cinzel", serif;
    font-size: 50px;
    letter-spacing: 2px;
    line-height: 1;
    color: var(--copper-light);
  }
  .origin-line {
    position: absolute;
    left: 305px;
    width: 519px;
    top: 542px;
    text-align: center;
    font-size: 35px;
    font-weight: 500;
    color: var(--soft-white);
    letter-spacing: -0.5px;
  }
  .net-weight {
    position: absolute;
    left: 305px;
    width: 519px;
    top: 600px;
    text-align: center;
    font-size: 19px;
    color: var(--soft-white);
  }
  .web-bar {
    position: absolute;
    left: 310px;
    top: 660px;
    width: 509px;
    height: 65px;
    background: linear-gradient(90deg, var(--copper) 0%, var(--copper-light) 100%);
  }
  .small-bee {
    position: absolute;
    left: 72px;
    top: -16px;
    width: 72px;
    height: 60px;
    border-radius: 50%;
    background: radial-gradient(ellipse at center, #5a4a3a 0%, #d9d0c4 50%, rgba(217,208,196,0) 72%);
  }
  .web-address {
    position: absolute;
    left: 137px;
    top: 14px;
    font-size: 27px;
    color: var(--cream);
    letter-spacing: -0.3px;
  }
</style>
</head>
<body>
  <div class="label">
    <div class="label-frame"></div>
    <div class="bee-illustration" role="img" aria-label="Gold honey bee flying in profile"></div>

    <div class="brand-name">Lark &amp; Dew</div>

    <div class="quality-note">PURE &amp; NATURAL</div>
    <div class="product-name">RAW HONEY</div>

    <div class="origin-line">Made by Florida Bees</div>
    <div class="net-weight">NET WT 12oz (340g)</div>

    <div class="web-bar">
      <div class="small-bee" role="img" aria-label="Small pair of honey bees"></div>
      <div class="web-address">larkanddewhoney.com</div>
    </div>
  </div>
</body>
</html>
```